Tidewell Recovery Business Card Design

Professional and clean design. The design colors should flow with the logo. Two-sided card with the website on the back which is:

www.TidewellRecovery.example.

"Specializing in Water Damage Restoration"

On the front I need the name, email, phone, and logo.

Name: Dorian Vashti
Email: Dorian@TidewellRecovery.example
Phone: 555-318-2046 for now

I only have the Preview and Thumbnail right now but should have the source files uploaded within a day or two.

Target Market(s)

Flood victims, home owners with water damage from busted pipes etc...

Industry/Entity Type

Business

Contact Information for Business Card

Name: Dorian Vashti

Font styles to use
Serif
Sans Serif

```html
<!DOCTYPE html>
<html lang="en">
<head>
<meta charset="utf-8">
<title>Tidewell Recovery Business Card</title>
<link href="https://fonts.googleapis.com/css2?family=Cinzel:wght@400;600&family=Crimson+Text:wght@400&display=swap" rel="stylesheet">
<style>
  :root {
    --brand-blue: #2a9ad6;
    --brand-blue-light: #56c0ee;
    --brand-blue-faint: rgba(255,255,255,0.12);
    --card-white: #ffffff;
    --page-bg: #e9ecef;
    --ink-blue: #1f8fd0;
  }
  * { box-sizing: border-box; margin: 0; padding: 0; }
  html, body { width: 1200px; height: 780px; overflow: hidden; }
  body {
    background: var(--page-bg);
    display: flex;
    flex-direction: column;
    align-items: center;
    justify-content: center;
    gap: 40px;
  }
  .card {
    position: relative;
    width: 600px;
    height: 343px;
    overflow: hidden;
    box-shadow: 0 6px 18px rgba(0,0,0,0.18);
  }

  /* Back side */
  .card-back { background: var(--brand-blue); color: var(--card-white); }
  .card-back .backdrop-circle {
    position: absolute;
    left: 190px; top: -20px;
    width: 300px; height: 300px;
    border-radius: 50%;
    background: var(--brand-blue-faint);
  }
  .back-content {
    position: absolute; inset: 0;
    display: flex; flex-direction: column;
    align-items: center; justify-content: center;
  }
  .brand-dot {
    width: 46px; height: 46px; border-radius: 50%;
    background: var(--card-white);
    margin-bottom: 10px;
  }
  .brand-name {
    font-family: "Cinzel", serif;
    font-weight: 600;
    font-size: 40px;
    letter-spacing: 2px;
    line-height: 1;
  }
  .brand-sub {
    display: flex; align-items: center; gap: 8px;
    font-family: "Cinzel", serif;
    font-size: 13px;
    letter-spacing: 6px;
    margin-top: 4px;
  }
  .brand-sub::before, .brand-sub::after {
    content: ""; width: 36px; height: 1.5px; background: currentColor;
  }
  .back-web {
    font-family: "Crimson Text", serif;
    font-size: 15px;
    margin-top: 20px;
  }

  /* Front side */
  .card-front { background: var(--card-white); }
  .front-curve { position: absolute; inset: 0; }
  .front-content {
    position: absolute; left: 44px; top: 58px;
    color: var(--ink-blue);
  }
  .front-brand { display: flex; align-items: center; gap: 14px; }
  .front-brand .brand-dot { background: var(--ink-blue); margin: 0; width: 50px; height: 50px; }
  .front-brand .brand-name { font-size: 36px; }
  .front-brand .brand-sub { font-size: 12px; letter-spacing: 6px; }
  .tagline {
    font-family: "Crimson Text", serif;
    font-size: 14px;
    margin-top: 6px;
  }
  .person-name {
    font-family: "Cinzel", serif;
    font-size: 22px;
    letter-spacing: 1px;
    margin-top: 26px;
  }
  .contact-list { list-style: none; margin-top: 14px; }
  .contact-list li {
    display: flex; align-items: center; gap: 8px;
    font-family: "Crimson Text", serif;
    font-size: 16px;
    line-height: 1.35;
  }
  .contact-list svg { width: 14px; height: 14px; fill: none; stroke: var(--ink-blue); stroke-width: 1.6; }
</style>
</head>
<body>

  <section class="card card-back" aria-label="Card back">
    <div class="backdrop-circle"></div>
    <div class="back-content">
      <div class="brand-dot"></div>
      <div class="brand-name">TIDEWELL</div>
      <div class="brand-sub">RECOVERY</div>
      <div class="back-web">www.TidewellRecovery.example</div>
    </div>
  </section>

  <section class="card card-front" aria-label="Card front">
    <svg class="front-curve" viewBox="0 0 600 343" preserveAspectRatio="none">
      <rect width="600" height="343" fill="var(--card-white)"/>
      <path d="M420 0 L600 0 L600 343 L470 343 C560 250 570 90 420 0 Z" fill="var(--brand-blue-light)"/>
      <path d="M450 0 L600 0 L600 343 L505 343 C590 250 600 90 450 0 Z" fill="var(--card-white)"/>
      <path d="M462 0 L600 0 L600 343 L520 343 C605 250 612 90 462 0 Z" fill="var(--brand-blue)"/>
    </svg>
    <div class="front-content">
      <div class="front-brand">
        <div class="brand-dot"></div>
        <div>
          <div class="brand-name">TIDEWELL</div>
          <div class="brand-sub">RECOVERY</div>
        </div>
      </div>
      <p class="tagline">Specializing in Water Damage Restoration</p>
      <p class="person-name">DORIAN VASHTI</p>
      <ul class="contact-list">
        <li><svg viewBox="0 0 16 16"><path d="M3 2h3l1 3-2 1a8 8 0 0 0 5 5l1-2 3 1v3c0 1-1 1-1 1C7 14 2 9 2 3c0 0 0-1 1-1z"/></svg>555-318-2046</li>
        <li><svg viewBox="0 0 16 16"><rect x="1.5" y="3.5" width="13" height="9"/><path d="M1.5 3.5 8 9l6.5-5.5"/></svg>Dorian@TidewellRecovery.example</li>
        <li><svg viewBox="0 0 16 16"><rect x="1.5" y="2.5" width="13" height="9"/><path d="M6 14h4M8 11.5V14"/></svg>www.TidewellRecovery.example</li>
      </ul>
    </div>
  </section>

</body>
</html>
```